Floorplan brochure design for rental company

We need a brochure designed for our rental company, Bramble Tor Commons.
We have two different categories that we need on this brochure: townhomes (primary) and mobile homes. Size and layout is up to you... choose what you think works best for the information being presented. However, please do not use an odd shape or size; do use a size and format that can be printed by qelvaprint.com.
Font and color choices are up to you. If needed, the fonts from the logo are Americana Extra Bold and BlackJack.
Industry/Entity Type
It Company
Requirements
Must have
- 1. logo and office address/contact information
2. floorplans and prices from attached documents
3. amenities from attached document
Should not have
- Please do not use our website, brambletor.com, as a basis for any design or color scheme decisions. We are working on a redesign of that website with our new logo (attached).

```html
<!DOCTYPE html>
<html lang="en">
<head>
<meta charset="utf-8">
<title>Bramble Tor Commons Brochure</title>
<link href="https://fonts.googleapis.com/css2?family=Source+Sans+3:wght@400;600;700&family=Roboto+Condensed:wght@700&display=swap" rel="stylesheet">
<style>
  :root{
    --blue:#0a9ac8;
    --green:#3f9a3a;
    --ink:#5a5a5a;
    --dark:#222;
    --rule:#333;
    --red:#d0312d;
    --paper:#fff;
  }
  *{margin:0;padding:0;box-sizing:border-box}
  html,body{width:1200px;height:927px;overflow:hidden;background:var(--paper)}
  .sheet{position:relative;width:1200px;height:927px;font-family:"Source Sans 3",Arial,sans-serif;color:var(--ink)}
  .band-blue{position:absolute;left:0;top:0;width:47px;height:927px;background:var(--blue)}
  .band-green{position:absolute;left:47px;top:0;width:17px;height:927px;background:var(--green)}
  .fold{position:absolute;left:600px;top:0;width:2px;height:927px;background:var(--rule)}
  .frame-top{position:absolute;left:64px;top:0;width:1136px;height:1px;background:#999}
  .heading{font-family:"Roboto Condensed",Arial,sans-serif;font-weight:700;color:var(--blue);letter-spacing:.5px}
  .amenities{position:absolute;left:97px;top:38px;width:400px}
  .amenities .heading{font-size:38px;line-height:46px}
  .amenities dl{font-size:11.5px;line-height:14.6px;margin-top:2px}
  .amenities dt{font-weight:700}
  .amenities dd + dt{margin-top:14.6px}
  .note{color:var(--red)}
  .note-text{color:var(--red);font-style:italic}
  .brand-small{position:absolute;left:190px;top:600px;width:200px;text-align:center}
  .brand-name{font-family:"Source Sans 3",Arial,sans-serif;font-weight:700;color:var(--green)}
  .brand-small .brand-name{font-size:22px;line-height:26px}
  .brand-mark{display:inline-block;border-radius:50%;background:var(--green)}
  .brand-small .brand-mark{width:46px;height:46px;margin-bottom:10px}
  .contacts{position:absolute;left:190px;top:724px;width:210px;text-align:center;font-size:13px;line-height:16.3px}
  .contacts h2{font-size:13px;font-weight:700;color:var(--blue);margin-bottom:10px}
  .contacts strong{font-weight:700}
  .brand-large{position:absolute;left:680px;top:300px;width:420px;text-align:center}
  .brand-large .brand-mark{width:110px;height:110px;margin-bottom:28px}
  .brand-large .brand-name{font-size:50px;line-height:58px}
  .about{position:absolute;left:651px;top:612px;width:549px}
  .about-head{display:flex;align-items:center}
  .about-head .heading{font-size:38px;line-height:40px;white-space:nowrap}
  .about-head .line{flex:1;height:1px;background:var(--blue);margin-left:6px;margin-top:8px}
  .about p{width:476px;font-size:11.4px;line-height:13.8px;margin-top:8px}
  .about p + p{margin-top:13.8px}
  .web{position:absolute;left:651px;top:872px;width:476px;text-align:center;font-size:12px;font-weight:700;color:var(--dark)}
</style>
</head>
<body>
<div class="sheet">
  <div class="frame-top"></div>
  <div class="band-blue"></div>
  <div class="band-green"></div>
  <div class="fold"></div>

  <section class="amenities">
    <h1 class="heading">AMENITIES</h1>
    <dl>
      <dt>overall features:</dt>
      <dd>golf course<br>convenience store<br>gated access<br>playground<br>basketball courts<br>stocked fishing lake<br>pet friendly<span class="note">*</span><br>dog park<br>extra storage available<br>lawn care included<br>outdoor grills permitted<br><span class="note-text">*breed resitrictions</span></dd>
      <dt>townhomes:</dt>
      <dd>6 foot privacy fenced backyard<br>concrete backyard patio<br>assigned front door parking</dd>
      <dt>mobile homes:</dt>
      <dd>large fenced backyards<br>concrete patio<br>private driveway</dd>
    </dl>
  </section>

  <div class="brand-small">
    <span class="brand-mark"></span>
    <div class="brand-name">Bramble Tor Commons</div>
  </div>

  <section class="contacts">
    <h2>CONTACTS</h2>
    <strong>Mailing Address:</strong><br>
    1870 Marlow Lane<br>
    Fernhill, TX 77612<br>
    <strong>Phone Number:</strong><br>
    Office: 855-555-0147<br>
    <strong>Office Hours:</strong><br>
    Mon-Fri: 9:00am-6:00pm<br>
    Sat: 9:00am-5:00pm
  </section>

  <div class="brand-large">
    <span class="brand-mark"></span>
    <div class="brand-name">Bramble Tor Commons</div>
  </div>

  <section class="about">
    <div class="about-head"><h2 class="heading">ABOUT US</h2><span class="line"></span></div>
    <p>We offer affordable townhomes, duplexes, houses, and mobile homes for rent. All feature private fenced-in yards, perfect if you have children or pets... or if you just need more room and privacy than traditional apartments can offer. And at Bramble Tor Commons, we offer more than just great features and prices - our philosophy here is service, featuring superb customer care and quick maintenance response. All of these things together result in a first-rate quality of living. The Bramble Tor Commons community amenities include The Links at Bramble Tor, a 9-hole par-3 lighted golf course. The newly opened Tor Oven: Pizza &amp; Pub offers delivery, dine-in, and carry-out service and bar. Bramble Tor Mini Storage facility offers affordable and convenient storage units. And finally, Bramble Tor Commons has a full convenience store with new release DVD rentals available every week.</p>
    <p>We pride ourselves in our quality and service, and we know that if you choose Bramble Tor Commons to be your next home you'll love living here because of it.</p>
  </section>

  <div class="web">www.brambletorcommons.com</div>
</div>
</body>
</html>
```